Logo & Responsive Website Design for Mortgage Company

Vantor Mortgage is a new Mortgage Fin-Tech company that will use its own innovative, proprietary technology for lead generation, mortgage origination, and processing of residential home loans in the US. The design should convey that we are a technology-driven company, offering borrowers seeking home loans an exceptional experience throughout the borrowing process.

We are looking for designs that are elegant, convey technical competency, simple to navigate, and set us apart from the competition.

We are not set on any particular colors at this point, so feel free to choose the best colors for your particular designs.

Please include both desktop and mobile designs.

Some Examples of Mortgage Websites. These are to show the typical content, not designs that we particularly like or dislike.
https://www.plumvane.com/
https://www.qbtfunding.com/
https://dorvelmortgage.com/
https://kelvo.com/
https://corvabaylending.com/

Please send comments with additional questions.

Thank You For your participation.

Target Market(s)

U.S. Residential Home Loan Seekers

Industry/Entity Type

FinTech Mortgage

Number of Pages Required

2 page

```html
<!DOCTYPE html>
<html lang="en">
<head>
<meta charset="utf-8">
<title>Mortgage – Get a Great Mortgage Rate</title>
<link href="https://fonts.googleapis.com/css2?family=Poppins:wght@400;500;600;700&display=swap" rel="stylesheet">
<style>
:root{
  --green:#2f8a48;
  --green-title:#5ba734;
  --lime:#cce97f;
  --lime-dark:#b7dc5e;
  --dark:#353130;
  --ink:#333333;
  --muted:#666666;
  --line:#d9d9d9;
  --grey-bg:#f3f3f3;
  --white:#ffffff;
}
*{box-sizing:border-box;margin:0;padding:0}
html,body{width:1200px;height:4440px;overflow:hidden}
body{position:relative;font-family:'Poppins',sans-serif;color:var(--ink);background:var(--white)}
.abs{position:absolute}
section,header,footer{position:absolute;left:0;width:1200px}

/* nav */
.site-nav{top:0;height:60px;background:var(--white)}
.brand{left:55px;top:12px;font-size:30px;font-weight:600;color:#444}
.nav-links{left:264px;top:20px;display:flex;gap:0;font-size:11px;color:#555}
.nav-links span{position:absolute;white-space:nowrap}
.btn-apply{left:957px;top:15px;width:72px;height:23px;border-radius:12px;background:var(--lime);color:var(--green);font-size:11px;display:flex;align-items:center;justify-content:center}
.nav-phone{left:1043px;top:18px;font-size:11px;color:#555;display:flex;align-items:center;gap:5px}

/* hero */
.hero{top:60px;height:531px;background:var(--green)}
.hero-title{left:121px;top:152px;font-size:41px;line-height:52px;font-weight:600;color:var(--white)}
.hero-sub{left:121px;top:270px;font-size:12px;line-height:20px;color:var(--white)}
.btn-pill{height:50px;border-radius:25px;font-size:12.5px;display:flex;align-items:center;justify-content:center}
.btn-fill{left:121px;top:330px;width:201px;background:var(--lime);color:var(--green)}
.btn-outline{left:345px;top:330px;width:176px;border:2px solid var(--lime);color:var(--lime)}
.hero-art{left:612px;top:78px;width:466px;height:379px;border-radius:24px;background:linear-gradient(135deg,#e8efe9,#c6d9c9 55%,#d6e96b);opacity:.9}

/* calculator */
.calculator{top:591px;height:147px;background:var(--dark);color:var(--white)}
.calc-title{left:0;width:1200px;top:26px;text-align:center;font-size:12px}
.calc-field{top:66px;width:267px}
.calc-field label{display:block;font-size:7px;margin-bottom:3px}
.calc-field .input{height:26px;background:var(--white);color:#777;font-size:8px;padding:8px 8px}

/* headings */
.section-title{font-size:26px;font-weight:600;color:var(--green-title)}
.body-text{font-size:10px;line-height:15px;color:#555}

/* about */
.about{top:738px;height:520px}
.art-about{left:517px;top:124px;width:526px;height:328px;border-radius:40% 45% 30% 35%;background:linear-gradient(160deg,#f1f1f1,#e4efe0 60%,#c6e38c)}

/* how */
.how{top:1258px;height:430px}
.how .section-title{left:0;width:1200px;top:44px;text-align:center}
.how-sub{left:397px;top:100px;width:408px;text-align:center}
.step{top:196px;width:210px;text-align:center}
.step-icon{width:76px;height:76px;border-radius:50%;background:var(--lime);margin:0 auto;display:flex;align-items:center;justify-content:center}
.step h3{font-size:11px;font-weight:500;margin-top:19px;color:#444}
.step p{margin-top:10px;font-size:9.5px;line-height:14px;color:#555}

/* today rate */
.rate{top:1700px;height:440px}
.lender-list{left:252px;top:82px;font-size:15px;color:#444}
.lender-list li{list-style:none;height:49px}
.rate-card{left:402px;top:58px;width:255px;height:263px;border-radius:6px;background:linear-gradient(160deg,#2a2626,#1a1717 60%,#3a1515)}
.rate .section-title{left:715px;top:108px}
.rate .body-text{left:715px;top:164px;width:228px}

/* tools */
.tools{top:2145px;height:424px;background:var(--dark)}
.tools .section-title{left:245px;top:50px;color:var(--green-title)}
.tool-item{left:245px;width:420px;height:80px}
.tool-icon{position:absolute;left:0;top:0;width:74px;height:74px;border-radius:50%;border:1.5px solid #bbb;display:flex;align-items:center;justify-content:center}
.tool-icon.active{background:var(--green-title);border-color:var(--green-title)}
.tool-item h3{position:absolute;left:98px;top:4px;font-size:11px;font-weight:500;color:#ddd}
.tool-item p{position:absolute;left:98px;top:30px;width:300px;font-size:9.5px;line-height:15px;color:#ccc}
.loan-card{left:710px;top:117px;width:247px;height:307px;background:var(--white);border-radius:6px 6px 0 0;padding:0 22px}
.loan-card .t{position:absolute;font-size:9px;color:#444}
.see-rate{position:absolute;left:150px;width:74px;height:22px;border-radius:11px;background:var(--lime);color:var(--green);font-size:9px;display:flex;align-items:center;justify-content:center}

/* guide */
.guide{top:2569px;height:660px}
.guide .section-title{left:245px;top:122px;font-size:28px;line-height:35px}
.guide .body-text{left:245px;top:208px;width:228px}
.btn-small{height:20px;border-radius:10px;background:var(--lime);color:var(--green);font-size:9px;display:flex;align-items:center;justify-content:center}
.guide .btn-small{left:245px;top:327px;width:105px}
.art-guide{left:577px;top:148px;width:380px;height:196px;border-radius:10px;background:linear-gradient(135deg,#f2f2f2,#dcebd7 55%,#ecd25d)}
.faq{left:577px;top:378px;width:376px}
.faq-row{height:41px;border-bottom:1px solid var(--line);display:flex;align-items:center;justify-content:space-between;font-size:9px;color:#444;padding-right:4px}

/* reviews */
.reviews{top:3229px;height:426px}
.reviews .section-title{left:276px;top:50px}
.score{left:276px;top:88px;font-size:42px;font-weight:600;color:var(--green)}
.stars{color:var(--green-title);font-size:12px;letter-spacing:2px}
.review{width:205px}
.review h4{font-size:12px;font-weight:500;margin-top:6px;color:#333}
.review p{font-size:9.5px;line-height:13.3px;margin-top:6px;color:#555}
.review .by{font-size:7.5px;margin-top:6px;color:#333}
.review .by em{font-style:normal;color:var(--green-title);margin-left:8px}
.review .loc{font-size:7.5px;color:#777}
.arrow{font-size:18px;color:#444}

/* partners */
.partners{top:3655px;height:293px;background:var(--grey-bg)}
.partners-label{left:0;width:1200px;top:78px;text-align:center;font-size:12px;color:#444}
.partner-pill{top:145px;height:72px;border-radius:36px;background:#d8d8d8}

/* cta */
.cta{top:3948px;height:238px;background:var(--green);color:var(--white)}
.cta-title{left:0;width:1200px;top:64px;text-align:center;font-size:26px;font-weight:600}
.cta .btn-small{left:546px;top:112px;width:106px}
.cta-text{left:0;width:1200px;top:160px;text-align:center;font-size:9px;line-height:14px}

/* footer */
.site-footer{top:4186px;height:254px;background:var(--dark);color:#ddd}
.foot-brand{left:276px;top:58px;font-size:19px;font-weight:600;color:var(--white)}
.foot-about{left:276px;top:96px;width:190px;font-size:9.5px;line-height:14px}
.foot-col{top:70px;font-size:9.5px}
.foot-col h4{font-size:10.5px;font-weight:500;color:var(--white);margin-bottom:12px}
.foot-col li{list-style:none;height:29.5px}
.foot-contact{left:821px;top:70px;font-size:9px;line-height:14px;width:140px}
.foot-contact h4{font-size:10.5px;font-weight:500;color:#ccc;margin-bottom:12px}
.social{display:flex;gap:14px;margin-top:14px}
.social span{width:14px;height:14px;border-radius:50%;border:1.5px solid #ddd}
</style>
</head>
<body>

<header class="site-nav">
  <div class="abs brand">Mortgage</div>
  <nav class="abs nav-links">
    <span style="left:0">Home</span>
    <span style="left:66px">About Us</span>
    <span style="left:150px">Purchase</span>
    <span style="left:236px">Refinance</span>
    <span style="left:330px">Today's Rate</span>
    <span style="left:439px">Loan Option</span>
    <span style="left:542px">Free Tools</span>
    <span style="left:632px">Support</span>
  </nav>
  <div class="abs btn-apply">Apply</div>
  <div class="abs nav-phone">
    <svg width="14" height="14" viewBox="0 0 24 24"><path fill="#2f8a48" d="M6.6 10.8a15.1 15.1 0 0 0 6.6 6.6l2.2-2.2a1 1 0 0 1 1-.25 11.4 11.4 0 0 0 3.6.57 1 1 0 0 1 1 1V20a1 1 0 0 1-1 1A17 17 0 0 1 3 4a1 1 0 0 1 1-1h3.5a1 1 0 0 1 1 1c0 1.25.2 2.45.57 3.6a1 1 0 0 1-.25 1z"/></svg>
    (602) 555-0148
  </div>
</header>

<section class="hero">
  <h1 class="abs hero-title">Get a Great<br>Mortgage Rate</h1>
  <p class="abs hero-sub">Use one of our quick &amp; easy tools to find out<br>what you qualify for, FREE!</p>
  <div class="abs btn-pill btn-fill">Home Purchase &nbsp;Qualifier</div>
  <div class="abs btn-pill btn-outline">Refine Rate Checker</div>
  <div class="abs hero-art" role="img" aria-label="Isometric illustration of a bank, calculator, percent sign, coins and people handling a loan"></div>
</section>

<section class="calculator">
  <div class="abs calc-title">Calculator</div>
  <div class="abs calc-field" style="left:59px"><label>Purchase Price</label><div class="input">$</div></div>
  <div class="abs calc-field" style="left:330px"><label>Down Payment</label><div class="input">%</div></div>
  <div class="abs calc-field" style="left:602px"><label>Loan Program</label><div class="input">30 year fixed</div></div>
  <div class="abs calc-field" style="left:873px"><label>Rate</label><div class="input">%</div></div>
</section>

<section class="about">
  <h2 class="abs section-title" style="left:252px;top:206px">About Us</h2>
  <p class="abs body-text" style="left:252px;top:262px;width:228px">Sed do eiusmod tempor incididunt ut labore et dolore magna aliqua. Ut enim ad minim veniam, quis nostrud exercitation ullamco laboris nisi ut aliquip ex ea commodo consequat. Duis aute irure dolor in reprehenderit in voluptate velit esse cillum dolore eu fugiat nulla pariatur.</p>
  <div class="abs art-about" role="img" aria-label="Illustration of a team feeding customers into a funnel machine that turns them into coins"></div>
</section>

<section class="how">
  <h2 class="abs section-title">How It Works</h2>
  <p class="abs body-text how-sub">Ut enim ad minim veniam, quis nostrud exercitation ullamco laboris nisi ut aliquip ex ea commodo consequat.</p>
  <div class="abs step" style="left:240px">
    <div class="step-icon"><svg width="34" height="34" viewBox="0 0 34 34" fill="none" stroke="#2f8a48" stroke-width="1.6"><path d="M17 5v22M9 27h16M6 11h22M6 11l-4 9h8zM28 11l-4 9h8z"/></svg></div>
    <h3>Excepteur sint occaecat</h3>
    <p>Ut enim ad minim veniam, quis nostrud exercitation ullamco laboris nisi ut aliquip ex ea commodo consequat.</p>
  </div>
  <div class="abs step" style="left:495px">
    <div class="step-icon"><svg width="34" height="34" viewBox="0 0 34 34" fill="none" stroke="#2f8a48" stroke-width="1.6"><rect x="5" y="14" width="12" height="16" rx="2"/><path d="M8 18h6M8 22h6M8 26h6"/><path d="M20 10c-3 4-3 10 4 10s7-6 4-10z"/><path d="M22 10l2-4 2 4"/></svg></div>
    <h3>Excepteur sint occaecat</h3>
    <p>Ut enim ad minim veniam, quis nostrud exercitation ullamco laboris nisi ut aliquip ex ea commodo consequat.</p>
  </div>
  <div class="abs step" style="left:747px">
    <div class="step-icon"><svg width="34" height="34" viewBox="0 0 34 34" fill="none" stroke="#2f8a48" stroke-width="1.6"><path d="M12 10c-6 5-7 18 5 18s11-13 5-18z"/><path d="M13 10l-2-5h12l-2 5"/><path d="M13 22l8-8"/><circle cx="14" cy="15" r="1.5"/><circle cx="20" cy="21" r="1.5"/></svg></div>
    <h3>Excepteur sint occaecat</h3>
    <p>Ut enim ad minim veniam, quis nostrud exercitation ullamco laboris nisi ut aliquip ex ea commodo consequat.</p>
  </div>
</section>

<section class="rate">
  <ul class="abs lender-list">
    <li>Logo name</li><li>Logo name</li><li>Logo name</li><li>Logo name</li><li>Logo name</li>
  </ul>
  <div class="abs rate-card" role="img" aria-label="Dark rate chart showing a 15 year fixed rate of 3.06 percent"></div>
  <h2 class="abs section-title">Today Rate</h2>
  <p class="abs body-text">Sed do eiusmod tempor incididunt ut labore et dolore magna aliqua. Ut enim ad minim veniam, quis nostrud exercitation ullamco laboris nisi ut aliquip ex ea commodo consequat. Duis aute irure dolor in reprehenderit in voluptate velit esse cillum dolore eu fugiat nulla pariatur.</p>
</section>

<section class="tools">
  <h2 class="abs section-title">Use Our Free Tool</h2>
  <div class="abs tool-item" style="top:104px">
    <div class="tool-icon active"><svg width="30" height="30" viewBox="0 0 34 34" fill="none" stroke="#fff" stroke-width="1.6"><path d="M12 10c-6 5-7 18 5 18s11-13 5-18z"/><path d="M13 10l-2-5h12l-2 5"/><path d="M13 22l8-8"/></svg></div>
    <h3>Excepteur sint occaecat</h3>
    <p>Ut enim ad minim veniam, quis nostrud exercitation ullamco laboris nisi ut aliquip ex ea commodo consequat.</p>
  </div>
  <div class="abs tool-item" style="top:202px">
    <div class="tool-icon"><svg width="30" height="30" viewBox="0 0 34 34" fill="none" stroke="#ddd" stroke-width="1.6"><rect x="5" y="14" width="12" height="16" rx="2"/><path d="M8 18h6M8 22h6M8 26h6"/><path d="M20 10c-3 4-3 10 4 10s7-6 4-10z"/></svg></div>
    <h3>Excepteur sint occaecat</h3>
    <p>Ut enim ad minim veniam, quis nostrud exercitation ullamco laboris nisi ut aliquip ex ea commodo consequat.</p>
  </div>
  <div class="abs tool-item" style="top:300px">
    <div class="tool-icon"><svg width="30" height="30" viewBox="0 0 34 34" fill="none" stroke="#ddd" stroke-width="1.6"><path d="M4 16L15 6l11 10M7 14v14h12"/><circle cx="24" cy="24" r="6"/><path d="M24 21v6"/></svg></div>
    <h3>Excepteur sint occaecat</h3>
    <p>Ut enim ad minim veniam, quis nostrud exercitation ullamco laboris nisi ut aliquip ex ea commodo consequat.</p>
  </div>
  <div class="abs loan-card">
    <div class="t" style="left:22px;top:19px">‹ &nbsp;&nbsp;Select your loan</div>
    <div class="t" style="left:22px;top:64px;font-size:8px">Lender</div>
    <div class="t" style="left:22px;top:84px;font-size:11px">30 Years Fixed</div>
    <div class="abs" style="left:22px;top:110px;width:204px;height:2px;background:var(--lime-dark)"></div>
    <div class="t" style="left:22px;top:145px;font-size:8px">Lender</div>
    <div class="t" style="left:176px;top:145px;font-size:8px">Rate</div>
    <div class="t" style="left:22px;top:182px">› &nbsp;Hallow Lending</div><div class="see-rate" style="top:177px;left:150px">See rate</div>
    <div class="t" style="left:22px;top:230px">› &nbsp;Hallow Lending</div><div class="see-rate" style="top:225px;left:150px">See rate</div>
    <div class="t" style="left:22px;top:278px">› &nbsp;Hallow Lending</div><div class="see-rate" style="top:273px;left:150px">See rate</div>
  </div>
</section>

<section class="guide">
  <h2 class="abs section-title">We’re always here<br>to guide yout</h2>
  <p class="abs body-text">Sed do eiusmod tempor incididunt ut labore et dolore magna aliqua. Ut enim ad minim veniam, quis nostrud exercitation ullamco laboris nisi ut aliquip ex ea commodo consequat. Duis aute irure dolor in reprehenderit in voluptate velit esse cillum dolore eu fugiat nulla pariatur.</p>
  <div class="abs btn-small">Schedule a call</div>
  <div class="abs art-guide" role="img" aria-label="Illustration of two people beside a large calculator and a money bag"></div>
  <div class="abs faq">
    <div class="faq-row">Sed ut perspiciatis unde ?<span>›</span></div>
    <div class="faq-row">Sed ut perspiciatis unde ?<span>›</span></div>
    <div class="faq-row">Sed ut perspiciatis unde ?<span>›</span></div>
    <div class="faq-row">Sed ut perspiciatis unde ?<span>›</span></div>
    <div class="faq-row">Sed ut perspiciatis unde ?<span>›</span></div>
  </div>
</section>

<section class="reviews">
  <h2 class="abs section-title">What people are saying</h2>
  <div class="abs score">3.06</div>
  <div class="abs stars" style="left:276px;top:148px">★★★★★</div>
  <div class="abs" style="left:276px;top:178px;font-size:8.5px;line-height:13px;color:#555">435 verified<br>customer reviews</div>
  <div class="abs arrow" style="left:418px;top:138px">‹</div>
  <div class="abs review" style="left:443px;top:96px">
    <div class="stars">★★★★★</div>
    <h4>Very Efficient!</h4>
    <p>Sed do eiusmod tempor incididunt ut labore et dolore magna aliqua. Ut enim ad minim veniam, quis nostrud exercitation ullamco laboris nisi ut aliquip ex ea commodo consequat. Duis aute irure dolor in reprehenderit in voluptate velit esse cillum dolore eu fugiat nulla pariatur.</p>
    <div class="by">John Doe <em>Verified Reviewer</em></div>
    <div class="loc">Oklahoma, US (September 2022)</div>
  </div>
  <div class="abs review" style="left:700px;top:96px">
    <div class="stars">★★★★★</div>
    <h4>Excellent!</h4>
    <p>Sed do eiusmod tempor incididunt ut labore et dolore magna aliqua. Ut enim ad minim veniam, quis nostrud exercitation ullamco laboris nisi ut aliquip ex ea commodo consequat. Duis aute irure dolor in reprehenderit in voluptate velit esse cillum dolore eu fugiat nulla pariatur.</p>
    <div class="by">John Doe <em>Verified Reviewer</em></div>
    <div class="loc">Oklahoma, US (September 2022)</div>
  </div>
  <div class="abs arrow" style="left:915px;top:138px">›</div>
</section>

<section class="partners">
  <div class="abs partners-label">Our trusted partners</div>
  <div class="abs partner-pill" style="left:71px;width:189px"></div>
  <div class="abs partner-pill" style="left:291px;width:188px"></div>
  <div class="abs partner-pill" style="left:509px;width:187px"></div>
  <div class="abs partner-pill" style="left:721px;width:187px"></div>
  <div class="abs partner-pill" style="left:936px;width:190px"></div>
</section>

<section class="cta">
  <h2 class="abs cta-title">Take the first step to fast finance.</h2>
  <div class="abs btn-small">Get Started</div>
  <p class="abs cta-text">Have questions? Call us today and connect with one of our mortgage specialists.<br>080 555 014</p>
</section>

<footer class="site-footer">
  <div class="abs foot-brand">Mortgage</div>
  <p class="abs foot-about">Consectetur adipiscing elit, sed do eiusmod tempor incididunt ut labore et dolore magna aliqua</p>
  <div class="abs foot-col" style="left:546px"><h4>Quick Link</h4><ul><li>Labore</li><li>Dolore</li><li>Magna</li><li>Aliqua</li></ul></div>
  <div class="abs foot-col" style="left:688px"><h4>Services</h4><ul><li>Labore</li><li>Dolore</li><li>Magna</li><li>Aliqua</li></ul></div>
  <div class="abs foot-contact">
    <h4>Contact Info</h4>
    Duis aute irure dolor<br>in reprehenderit<br>+01 555 0192<br>info@lumorahq.com
    <div class="social"><span></span><span></span><span></span></div>
  </div>
</footer>

</body>
</html>
```